KORN Tax
Keystone Options and Revenue Navigators
KORN Tax  - Financial Services
Creative Brief
Professional
Tobias Whitlock, CPA CGA
President & CEO
47 Pellam Street Suite 2060 Harborview Court Dartmouth, NS B2C 7K9
rtw@korn.ca
www.korn.ca

```html
<!DOCTYPE html>
<html lang="en">
<head>
<meta charset="utf-8">
<title>KORN Tax — Stationery</title>
<link rel="stylesheet" href="https://fonts.googleapis.com/css2?family=Cinzel:wght@600&family=Open+Sans:wght@400;600&display=swap">
<style>
  :root{
    --bg:#ebebed;
    --paper:#ffffff;
    --navy:#173b8c;
    --blue:#2e74d8;
    --sky:#5d9cef;
    --ink:#4a4f5a;
    --muted:#8a8f99;
  }
  *{box-sizing:border-box;margin:0;padding:0}
  html,body{width:1200px;height:937px;overflow:hidden;background:var(--bg)}
  body{position:relative;font-family:"Open Sans",Arial,sans-serif;color:var(--ink)}
  .sheet{position:absolute;background:var(--paper);overflow:hidden}
  .wave{position:absolute;left:0;bottom:0;width:100%}
  .brand{font-family:"Cinzel",Georgia,serif;font-weight:600;color:var(--navy);display:flex;align-items:center;white-space:nowrap}
  .brand .mark{background:var(--navy);display:inline-block;flex:none}
  .tagline{font-family:"Cinzel",Georgia,serif;font-weight:600;color:var(--navy);letter-spacing:.02em;white-space:nowrap}

  /* letterhead */
  .letterhead{left:182px;top:63px;width:388px;height:549px}
  .letterhead .brand{position:absolute;left:38px;top:38px;font-size:17px;gap:7px}
  .letterhead .brand .mark{width:14px;height:14px}
  .letterhead .contact{position:absolute;right:32px;top:30px;font-size:5.5px;line-height:8px;text-align:right;color:var(--muted)}
  .letter{position:absolute;left:38px;top:110px;width:300px;font-size:5.5px;line-height:8.5px;color:var(--muted)}
  .letter p{margin-bottom:8px}
  .letter .sign-space{height:22px}
  .letter .signer{color:var(--ink);font-weight:600}

  /* folder */
  .folder{left:633px;top:51px;width:392px;height:561px}
  .folder .lockup{position:absolute;left:0;right:0;top:180px;text-align:center}
  .folder .brand{justify-content:center;font-size:40px;gap:14px}
  .folder .brand .mark{width:30px;height:30px}
  .folder .tagline{margin-top:8px;font-size:11.5px}

  /* business cards */
  .card{left:46px;width:177px;height:106px}
  .card-front{top:653px}
  .card-back{top:780px}
  .card .brand{position:absolute;font-size:11px;gap:5px}
  .card .brand .mark{width:9px;height:9px}
  .card-front .brand{left:12px;top:14px}
  .card-front .details{position:absolute;right:10px;top:12px;text-align:right;font-size:4.6px;line-height:6.6px;color:var(--muted)}
  .card-front .details .name{color:var(--navy);font-weight:600;font-size:5.5px}
  .card-back .brand{left:14px;top:24px}

  /* envelopes */
  .envelope{top:666px;width:430px;height:232px}
  .envelope-front{left:266px}
  .envelope-front .brand{position:absolute;left:20px;top:22px;font-size:21px;gap:9px}
  .envelope-front .brand .mark{width:17px;height:17px}
  .envelope-front .tagline{position:absolute;left:20px;top:52px;font-size:6.5px}
  .envelope-back{left:739px;width:425px}
  .envelope-back svg{position:absolute;inset:0;width:100%;height:100%}
</style>
</head>
<body>

<!-- Letterhead -->
<section class="sheet letterhead">
  <div class="brand"><span class="mark"></span>KORN Tax</div>
  <div class="contact">
    47 Pellam Street Suite 2060<br>
    Harborview Court<br>
    Dartmouth, NS B2C 7K9<br>
    rtw@korn.ca<br>
    www.korn.ca
  </div>
  <div class="letter">
    <p>March 4, 2024</p>
    <p>Client Name<br>Street Address, City</p>
    <p>Dear Client,</p>
    <p>Thank you for choosing our firm. We review your records with care and prepare clear returns, timely filings and practical advice that helps your business plan ahead with confidence.</p>
    <p>Please find enclosed a summary of the items we discussed and the documents we still require.</p>
    <p>Our team remains available for any questions. We look forward to working with you through the coming year and supporting your growth at every stage.</p>
    <p>Sincerely,</p>
    <div class="sign-space"></div>
    <p><span class="signer">Tobias Whitlock</span><br>President &amp; CEO</p>
  </div>
  <svg class="wave" height="130" viewBox="0 0 400 120" preserveAspectRatio="none" aria-hidden="true">
    <path d="M0 64 C120 22 280 10 400 0 L400 120 L0 120Z" fill="var(--sky)"/>
    <path d="M0 74 C130 32 280 20 400 9 L400 120 L0 120Z" fill="var(--paper)"/>
    <path d="M0 82 C135 40 285 28 400 16 L400 120 L0 120Z" fill="var(--blue)"/>
    <path d="M0 90 C140 50 290 38 400 26 L400 120 L0 120Z" fill="var(--navy)"/>
  </svg>
</section>

<!-- Presentation folder -->
<section class="sheet folder">
  <div class="lockup">
    <div class="brand"><span class="mark"></span>KORN Tax</div>
    <div class="tagline">Keystone Options and Revenue Navigators</div>
  </div>
  <svg class="wave" height="140" viewBox="0 0 400 120" preserveAspectRatio="none" aria-hidden="true">
    <path d="M0 64 C120 22 280 10 400 0 L400 120 L0 120Z" fill="var(--sky)"/>
    <path d="M0 74 C130 32 280 20 400 9 L400 120 L0 120Z" fill="var(--paper)"/>
    <path d="M0 82 C135 40 285 28 400 16 L400 120 L0 120Z" fill="var(--blue)"/>
    <path d="M0 90 C140 50 290 38 400 26 L400 120 L0 120Z" fill="var(--navy)"/>
  </svg>
</section>

<!-- Business card front -->
<section class="sheet card card-front">
  <div class="brand"><span class="mark"></span>KORN Tax</div>
  <div class="details">
    <span class="name">Tobias Whitlock, CPA CGA</span><br>
    President &amp; CEO<br>
    rtw@korn.ca<br>
    www.korn.ca
  </div>
  <svg class="wave" height="48" viewBox="0 0 400 120" preserveAspectRatio="none" aria-hidden="true">
    <path d="M0 60 C120 20 280 10 400 0 L400 120 L0 120Z" fill="var(--sky)"/>
    <path d="M0 72 C130 30 280 20 400 10 L400 120 L0 120Z" fill="var(--paper)"/>
    <path d="M0 84 C140 45 290 35 400 22 L400 120 L0 120Z" fill="var(--navy)"/>
  </svg>
</section>

<!-- Business card back -->
<section class="sheet card card-back">
  <div class="brand"><span class="mark"></span>KORN Tax</div>
</section>

<!-- Envelope front -->
<section class="sheet envelope envelope-front">
  <div class="brand"><span class="mark"></span>KORN Tax</div>
  <div class="tagline">Keystone Options and Revenue Navigators</div>
  <svg class="wave" height="80" viewBox="0 0 400 120" preserveAspectRatio="none" aria-hidden="true">
    <path d="M0 64 C120 22 280 10 400 0 L400 120 L0 120Z" fill="var(--sky)"/>
    <path d="M0 74 C130 32 280 20 400 9 L400 120 L0 120Z" fill="var(--paper)"/>
    <path d="M0 84 C140 46 290 34 400 22 L400 120 L0 120Z" fill="var(--navy)"/>
  </svg>
</section>

<!-- Envelope back -->
<section class="sheet envelope envelope-back">
  <svg viewBox="0 0 425 232" preserveAspectRatio="none" aria-hidden="true">
    <rect width="425" height="232" fill="var(--paper)"/>
    <path d="M0 60 L212 150 L425 60 L425 232 L0 232Z" fill="var(--navy)"/>
    <path d="M0 0 L212 112 L425 0" fill="none" stroke="#d4d6db" stroke-width="1.5"/>
  </svg>
</section>

</body>
</html>
```